I need a business card designed using the logo provided either vertical or horizontal......Crestmoor Property Partners is an Australian based real estate company that caters for the upper end of the market so the design of the business card "must reflect" the companies image!!
Colour combinations are optional but "must be realistic" and must be able to be accurately useable CMYK colours.
Please consider that any colours used "must be able to be used" and be suitable in following designs for "pull out banner signs" and "real estate signs".
The colours and the font in the attached designs are for example and other combinations are encouraged.
Target Market(s)
The High End of the Australian real estate market
Industry/Entity Type
Business
Contact Information for Business Card
Logo - Business Name - Director + Licensed Real Estate Agent - Mobile Number (Cell Phone) - Business Number - Fax - Email Address - Web address
Requirements
Must have
- Designs and colours (CMYK) that can easily be interpreted by an Australian printer.
Nice to have
- Some alternative ideas on colour and font..........the ones provided are ok and have been provided as an example but I am looking for alternative ideas
Should not have
- Loud, overly bright colours. Designs that do not reflect the professional standards of the business.
- Designs that look good on a computer monitor but can not be re-created on a printing press.............this is most important when it comes to shading etc.

```html
<!DOCTYPE html>
<html lang="en">
<head>
<meta charset="UTF-8">
<title>Crestmoor Property Partners – Business Card</title>
<link rel="stylesheet" href="https://fonts.googleapis.com/css2?family=Open+Sans:wght@400;600;700&display=swap">
<style>
  :root {
    --backdrop: #3b322d;
    --card: #2e2f31;
    --card-glow: #46484b;
    --accent: #3fa7d8;
    --text: #e9ebed;
    --text-soft: #cfd3d6;
  }
  * { margin: 0; padding: 0; box-sizing: border-box; }
  html, body {
    width: 1200px; height: 844px; overflow: hidden;
    background: var(--backdrop);
    font-family: "Open Sans", Arial, sans-serif;
  }
  .stage {
    position: relative; width: 1200px; height: 844px;
    display: flex; align-items: center; justify-content: center; gap: 60px;
  }
  .card {
    position: relative; width: 520px; height: 300px;
    background: radial-gradient(ellipse at 55% 40%, var(--card-glow) 0%, var(--card) 70%);
    box-shadow: 0 10px 30px rgba(0,0,0,.45);
  }
  /* Back: contact details */
  .card-back .brand {
    position: absolute; left: 36px; top: 108px; width: 170px;
    display: flex; align-items: center; gap: 10px;
  }
  .brand-mark { width: 14px; height: 14px; background: var(--accent); flex: none; }
  .brand-name {
    color: var(--accent); font-weight: 700; font-size: 17px; line-height: 1.2;
    text-transform: uppercase; letter-spacing: .5px;
  }
  .details { position: absolute; left: 238px; top: 52px; color: var(--text); }
  .person-name {
    color: var(--accent); font-weight: 600; font-size: 19px;
    text-transform: uppercase; letter-spacing: .3px;
  }
  .person-role { font-size: 14px; color: var(--text-soft); margin-top: 1px; }
  .address { font-size: 14px; line-height: 1.2; margin-top: 18px; }
  .contact-list { list-style: none; margin-top: 16px; }
  .contact-list li {
    display: flex; align-items: center; gap: 8px;
    font-size: 14.5px; line-height: 19px;
  }
  .contact-list svg { width: 12px; height: 12px; fill: var(--accent); flex: none; }
  /* Front: name only */
  .card-front .brand {
    position: absolute; inset: 0;
    display: flex; flex-direction: column; align-items: center; justify-content: center; gap: 14px;
  }
  .card-front .brand-mark { width: 22px; height: 22px; }
  .card-front .brand-name {
    color: var(--text); font-size: 24px; text-align: center; letter-spacing: 2px;
  }
</style>
</head>
<body>
<main class="stage">
  <section class="card card-back">
    <div class="brand">
      <span class="brand-mark"></span>
      <span class="brand-name">Crestmoor Property Partners</span>
    </div>
    <div class="details">
      <p class="person-name">Daniel Ashford</p>
      <p class="person-role">Managing Director</p>
      <p class="address">48 Harbour View Road<br>Mosman, NSW 2088</p>
      <ul class="contact-list">
        <li><svg viewBox="0 0 12 12"><path d="M2 1h2.5l1 3-1.5 1a7 7 0 0 0 3 3l1-1.5 3 1V11c-5 0-9-4-9-9z"/></svg>0412 738 205</li>
        <li><svg viewBox="0 0 12 12"><path d="M3 1h6v3H3zM1 5h10v6H1zm2 2v1h2V7zm4 0v1h2V7z"/></svg>02 9960 4521</li>
        <li><svg viewBox="0 0 12 12"><path d="M1 3h10v6H1zm1 .8L6 6.6l4-2.8V3.4L6 6 2 3.4z"/></svg>info@crestmoorpp.com.au</li>
        <li><svg viewBox="0 0 12 12"><path d="M4 7l3-3 1 1-3 3zM2.5 9.5a2 2 0 0 1 0-2.8L4 5.2l.8.8-1.5 1.5a.9.9 0 0 0 1.2 1.2L6 7.2l.8.8-1.5 1.5a2 2 0 0 1-2.8 0zm7-7a2 2 0 0 1 0 2.8L8 6.8 7.2 6l1.5-1.5a.9.9 0 0 0-1.2-1.2L6 4.8 5.2 4l1.5-1.5a2 2 0 0 1 2.8 0z"/></svg>www.crestmoorpp.com.au</li>
      </ul>
    </div>
  </section>
  <section class="card card-front">
    <div class="brand">
      <span class="brand-mark"></span>
      <span class="brand-name">Crestmoor<br>Property Partners</span>
    </div>
  </section>
</main>
</body>
</html>
```